Nu Shield Total Project

We are a wireless internet service provider (WISP). We are launching a new service to our customers called "Nu Shield Total". This new program will provide the following services to our customers as part of the $8.95 monthly service fee:
In-Home service calls are free
Provide WiFi Router
Router Support and Configuration
Free Cable Move (1 per year)
Cable Repair
Anti-Virus protection software
We will also be offering these services for additional charges:
Internet Security Suite $4.95 /month
Online Backup Storage - $4.99 /month
Target Market(s)
Current customers that use our internet service.
Industry/Entity Type
Wireless Internet
Look and feel
Each slider illustrates characteristics of the customer's brand and the style your logo design should communicate.

```html
<!DOCTYPE html>
<html lang="en">
<head>
<meta charset="utf-8">
<title>Nu Shield Total</title>
<link rel="stylesheet" href="https://fonts.googleapis.com/css2?family=Open+Sans:ital,wdth,wght@0,75..100,300..800;1,75..100,300..800&display=swap">
<style>
  :root {
    --navy: #0f2a83;
    --red: #d62236;
    --slate: #4a4a55;
    --grey: #8a8a8f;
    --tick: #1fc71f;
    --sky-top: #8f9db9;
    --sky-mid: #d5dae6;
    --paper: #ffffff;
    --swoosh: #c3cbe0;
  }
  html, body { margin: 0; padding: 0; overflow: hidden; }
  body { width: 1086px; height: 1200px; }
  .flyer {
    position: relative;
    width: 1086px;
    height: 1200px;
    overflow: hidden;
    font-family: "Open Sans", Arial, sans-serif;
    background: linear-gradient(180deg, var(--sky-top) 0%, var(--sky-mid) 28%, var(--paper) 62%, var(--paper) 100%);
  }
  .swooshes { position: absolute; inset: 0; }
  .title {
    position: absolute;
    top: 20px; left: 0; width: 1086px;
    margin: 0;
    text-align: center;
    font-size: 92px;
    font-weight: 800;
    font-style: italic;
    letter-spacing: 1px;
    text-shadow: 3px 4px 5px rgba(0,0,0,0.35);
  }
  .title .light { color: var(--paper); }
  .title .accent { color: var(--red); }
  .price {
    position: absolute;
    top: 160px; left: 126px;
    margin: 0;
    font-size: 58px;
    font-weight: 700;
    color: var(--navy);
  }
  .section-head {
    position: absolute;
    margin: 0;
    font-style: italic;
    font-weight: 600;
    font-stretch: 80%;
    color: var(--slate);
  }
  .includes-head { top: 314px; left: 86px; font-size: 52px; }
  .features {
    position: absolute;
    top: 404px; left: 190px;
    margin: 0; padding: 0;
    list-style: none;
  }
  .features li {
    display: flex;
    align-items: center;
    height: 60px;
    font-size: 43px;
    font-weight: 700;
    white-space: nowrap;
  }
  .features li svg { width: 58px; height: 50px; margin-right: 6px; flex: none; }
  .features .navy { color: var(--navy); }
  .features .red { color: var(--red); }
  .extras-head { top: 775px; left: 0; width: 1086px; text-align: center; font-size: 58px; }
  .extras {
    position: absolute;
    top: 848px; left: 0; width: 1086px;
    margin: 0;
    text-align: center;
    font-size: 37px;
    font-weight: 700;
    font-style: italic;
    line-height: 46px;
    color: var(--grey);
  }
  .brand {
    position: absolute;
    top: 1030px; left: 0; width: 1086px;
    text-align: center;
  }
  .brand-dot {
    display: block;
    width: 60px; height: 60px;
    margin: 0 auto 14px;
    border-radius: 50%;
    background: var(--red);
  }
  .brand-name {
    font-size: 44px;
    font-weight: 800;
    color: var(--navy);
    letter-spacing: 1px;
  }
  .base-rule { position: absolute; top: 1158px; height: 7px; background: var(--navy); }
  .base-rule.left { left: 0; width: 230px; }
  .base-rule.right { right: 0; width: 230px; }
</style>
</head>
<body>
<main class="flyer">
  <svg class="swooshes" width="1086" height="1200" viewBox="0 0 1086 1200" aria-hidden="true">
    <path d="M640 250 C820 230 960 200 1086 150 L1086 175 C960 222 820 246 640 250 Z" fill="#ffffff" opacity="0.9"/>
    <path d="M760 200 C880 190 990 170 1086 140 L1086 150 C990 178 880 194 760 200 Z" fill="#ffffff" opacity="0.7"/>
    <path d="M0 330 C140 320 320 340 520 360 C320 350 140 345 0 365 Z" fill="#ffffff" opacity="0.85"/>
    <path d="M0 1060 C120 990 280 960 420 965 C280 975 120 1010 0 1090 Z" fill="var(--swoosh)" opacity="0.7"/>
  </svg>

  <h1 class="title"><span class="light">Nu Shield</span> <span class="accent">Total</span></h1>
  <p class="price">$8.95 monthly</p>

  <h2 class="section-head includes-head">Package Includes:</h2>
  <ul class="features">
    <li class="navy"><svg viewBox="0 0 58 50"><path d="M4 28 L18 42 L54 6 L50 2 L18 32 L10 22 Z" fill="var(--tick)"/></svg>Anti-Virus protection software</li>
    <li class="red"><svg viewBox="0 0 58 50"><path d="M4 28 L18 42 L54 6 L50 2 L18 32 L10 22 Z" fill="var(--tick)"/></svg>In-Home service calls are free</li>
    <li class="navy"><svg viewBox="0 0 58 50"><path d="M4 28 L18 42 L54 6 L50 2 L18 32 L10 22 Z" fill="var(--tick)"/></svg>Provide WiFi Router</li>
    <li class="red"><svg viewBox="0 0 58 50"><path d="M4 28 L18 42 L54 6 L50 2 L18 32 L10 22 Z" fill="var(--tick)"/></svg>Router Support and Configuration</li>
    <li class="navy"><svg viewBox="0 0 58 50"><path d="M4 28 L18 42 L54 6 L50 2 L18 32 L10 22 Z" fill="var(--tick)"/></svg>Free Cable Move (1 per year)</li>
    <li class="red"><svg viewBox="0 0 58 50"><path d="M4 28 L18 42 L54 6 L50 2 L18 32 L10 22 Z" fill="var(--tick)"/></svg>Cable Repair</li>
  </ul>

  <h2 class="section-head extras-head">Additional Services:</h2>
  <p class="extras">Internet Security Suite $4.95 /month<br>Online Backup Storage - $4.99 /month</p>

  <div class="brand">
    <span class="brand-dot"></span>
    <span class="brand-name">MESA BREEZE WIRELESS</span>
  </div>
  <div class="base-rule left"></div>
  <div class="base-rule right"></div>
</main>
</body>
</html>
```